Brindle Works ~ Business Card Design Project

Brindle Works is a digital marketing agency which creates and maintains online social presence for brands and businesses. Services include monthly stream management, social media advertising campaigns, online press release distribution, search engine optimization, copywriting, digital strategy consultation, video marketing campaigns, fan acquisition, and Wordpress website development.
The company is currently rebranding to a full service agency from just a social media firm, with a new website launching soon. I'm looking for an extremely creative and modern business card design that pops out from the rest and fits with our company's sector/services.
It will need to be 1039 x 697 pixels, and rectangular (not rounded edges or corners). Utilize our company logo (file is attached), and include the following information in any design or layout:
Martin Okafor
CEO/Creative Director
Brindle Works
Facebook: fanpage.example/brindleworks
Twitter: @BrindleWorks
Phone: +1 555 014 8892
Cell: +1 555 017 4410
Email: martin@brindleworks.example
Website: www.brindleworks.example
418 Pellham Crescent, Suite 302
Marrow Bay, NR
K7Q 3V8

```html
<!DOCTYPE html>
<html lang="en">
<head>
<meta charset="utf-8">
<title>Brindle Works – Business Card</title>
<link href="https://fonts.googleapis.com/css2?family=Open+Sans:wght@400;600;700&display=swap" rel="stylesheet">
<style>
  :root {
    --stage: #b9bcc1;
    --card: #ffffff;
    --brand-blue: #2d55a9;
    --accent-red: #d3262c;
    --ink: #2f2f33;
  }
  * { box-sizing: border-box; margin: 0; padding: 0; }
  html, body { width: 1200px; height: 900px; overflow: hidden; }
  body {
    background: var(--stage);
    font-family: "Open Sans", Arial, sans-serif;
    color: var(--ink);
    position: relative;
  }
  .card {
    position: absolute;
    left: 340px;
    width: 520px;
    height: 349px;
    background: var(--card);
    overflow: hidden;
    box-shadow: 0 10px 24px rgba(0,0,0,0.18);
  }
  .card--front { top: 70px; }
  .card--back { top: 475px; }

  /* Front */
  .brand {
    position: absolute;
    left: 110px;
    top: 62px;
    display: flex;
    align-items: center;
    gap: 14px;
  }
  .brand__dot {
    width: 62px; height: 62px;
    border-radius: 50%;
    background: var(--brand-blue);
    flex: none;
  }
  .brand__name {
    font-size: 40px;
    font-weight: 700;
    color: var(--brand-blue);
    letter-spacing: -0.5px;
    white-space: nowrap;
  }
  .brand__web {
    position: absolute;
    left: 186px;
    top: 126px;
    font-size: 11px;
    font-weight: 600;
    color: var(--ink);
  }
  .band {
    position: absolute;
    left: 0; right: 0; bottom: 0;
    height: 108px;
    background: var(--brand-blue);
    color: #fff;
    display: flex;
    align-items: center;
    justify-content: space-between;
    padding: 0 34px;
    font-size: 12px;
  }
  .band__item { display: flex; align-items: center; gap: 8px; white-space: nowrap; }
  .band__icon {
    width: 14px; height: 14px;
    border: 1.5px solid #fff;
    border-radius: 3px;
  }

  /* Back */
  .card--back .brand { left: 36px; top: 30px; gap: 10px; }
  .card--back .brand__dot { width: 42px; height: 42px; }
  .card--back .brand__name { font-size: 28px; }
  .person { position: absolute; left: 36px; top: 100px; }
  .person__name { font-size: 22px; font-weight: 700; color: var(--brand-blue); }
  .person__title { font-size: 11px; color: var(--accent-red); margin-top: 2px; }
  .divider { position: absolute; left: 36px; top: 158px; }
  .contact {
    position: absolute;
    left: 36px; top: 180px;
    font-size: 12.5px;
    line-height: 21px;
    font-weight: 600;
    white-space: nowrap;
  }
  .contact__label { color: var(--accent-red); font-weight: 400; }
  .contact__indent { padding-left: 68px; }
  .stripe {
    position: absolute;
    left: 0; right: 0; bottom: 0;
    height: 22px;
    background: var(--brand-blue);
  }
</style>
</head>
<body>

<section class="card card--front" aria-label="Business card front">
  <div class="brand">
    <span class="brand__dot"></span>
    <span class="brand__name">Brindle Works</span>
  </div>
  <p class="brand__web">www.brindleworks.example</p>
  <div class="band">
    <span class="band__item">fanpage.example/brindleworks</span>
    <span class="band__item"><span class="band__icon"></span>@BrindleWorks</span>
  </div>
</section>

<section class="card card--back" aria-label="Business card back">
  <div class="brand">
    <span class="brand__dot"></span>
    <span class="brand__name">Brindle Works</span>
  </div>
  <div class="person">
    <p class="person__name">Martin Okafor</p>
    <p class="person__title">CEO/Creative Director</p>
  </div>
  <svg class="divider" width="200" height="8" viewBox="0 0 200 8" aria-hidden="true">
    <path d="M0 6 Q100 -2 200 6 Q100 2 0 6 Z" fill="var(--brand-blue)"/>
  </svg>
  <div class="contact">
    <p><span class="contact__label">ADDRESS:</span> 418 Pellham Crescent, Suite 302</p>
    <p class="contact__indent">Marrow Bay, NR K7Q 3V8</p>
    <p><span class="contact__label">P :</span> +1 555 014 8892 <span class="contact__label">| M :</span> +1 555 017 4410</p>
    <p><span class="contact__label">E :</span> martin@brindleworks.example</p>
  </div>
  <div class="stripe"></div>
</section>

</body>
</html>
```